Technology company needs an invitation for a Machine Learning Event

We need a invitation design for a technology company called Corvandel. We specialize on IT Services and Consulting and we're scheduling an Event on Machine Learning and Artificial Intelligence. Machine learning is a method of data analysis that automates analytical model building. It is a branch of artificial intelligence based on the idea that systems can learn from data, identify patterns and make decisions with minimal human intervention. It is the result of algorithmic implementations for data analysts to use. So basically, it provides systems the ability to automatically learn and improve from experience without being explicitly programmed to. Machine learning focuses on the development of computer programs that can access data and use it learn for themselves.
Colors
Designer to choose colors to be used in the design.
Look and feel

```html
<!DOCTYPE html>
<html lang="en">
<head>
<meta charset="utf-8">
<title>Corvandel – Machine Learning Event Invitation</title>
<link rel="stylesheet" href="https://fonts.googleapis.com/css2?family=Open+Sans:wght@400;600;700&display=swap">
<style>
  :root {
    --page-bg: #e6e6e6;
    --navy-deep: #141c58;
    --navy: #1c2b80;
    --navy-mid: #24399a;
    --dot-cyan: rgba(70, 170, 235, 0.55);
    --trace-cyan: rgba(60, 150, 215, 0.40);
    --glow-soft: rgba(140, 200, 255, 0.45);
    --accent-yellow: #f5b324;
    --brand-blue: #3b8fd8;
    --brand-dark: #2a2a2e;
    --brand-red: #d8402c;
    --silver-light: #ffffff;
    --silver-dark: #c4c8d1;
    --text-light: #ffffff;
    --faint-brand: rgba(90, 130, 210, 0.30);
  }
  * { box-sizing: border-box; margin: 0; padding: 0; }
  html, body {
    width: 1200px; height: 1200px; overflow: hidden;
    background: var(--page-bg);
    font-family: "Open Sans", Arial, sans-serif;
  }
  .invite-card {
    position: absolute;
    width: 728px; height: 536px;
    overflow: hidden;
    background: radial-gradient(ellipse at 50% 45%, var(--navy-mid) 0%, var(--navy) 50%, var(--navy-deep) 100%);
    box-shadow: 0 6px 18px rgba(0,0,0,0.35);
  }
  .invite-card--front { left: 82px; top: 58px; }
  .invite-card--back { left: 396px; top: 616px; }

  /* texture area: dotted corners, circuit traces and glows as soft tone fields */
  .circuit-art {
    position: absolute; inset: 0;
    background:
      radial-gradient(ellipse 150px 260px at 0% 12%, var(--dot-cyan) 0%, rgba(70,170,235,0.18) 55%, transparent 100%),
      radial-gradient(ellipse 150px 260px at 100% 12%, var(--dot-cyan) 0%, rgba(70,170,235,0.18) 55%, transparent 100%),
      radial-gradient(ellipse 90px 200px at 0% 85%, rgba(70,170,235,0.25) 0%, transparent 100%),
      radial-gradient(ellipse 90px 200px at 100% 85%, rgba(70,170,235,0.25) 0%, transparent 100%),
      radial-gradient(ellipse 380px 130px at 55% 88%, var(--trace-cyan) 0%, transparent 100%),
      radial-gradient(ellipse 260px 110px at 30% 62%, rgba(60,150,215,0.22) 0%, transparent 100%),
      radial-gradient(ellipse 260px 110px at 78% 58%, rgba(60,150,215,0.22) 0%, transparent 100%);
  }
  .glow {
    position: absolute; border-radius: 50%;
    background: radial-gradient(circle, var(--glow-soft) 0%, rgba(140,200,255,0.15) 45%, transparent 70%);
  }

  /* front */
  .brand-band {
    position: absolute; left: 0; top: 0; width: 100%; height: 156px;
    background: linear-gradient(90deg, rgba(201,204,211,0.2) 0%, var(--silver-dark) 10%, var(--silver-light) 30%, var(--silver-light) 70%, var(--silver-dark) 90%, rgba(201,204,211,0.2) 100%);
    display: flex; flex-direction: column; align-items: center; justify-content: center;
  }
  .brand-mark { width: 40px; height: 40px; border-radius: 50%; background: var(--brand-red); margin-bottom: 10px; }
  .brand-name { font-weight: 700; font-size: 32px; line-height: 1; color: var(--brand-dark); letter-spacing: 0.5px; }
  .brand-tagline { font-size: 11.5px; font-weight: 400; color: var(--brand-dark); margin-top: 5px; letter-spacing: 0.4px; }

  .event-title {
    position: absolute; top: 176px; left: 0; width: 100%;
    text-align: center; color: var(--accent-yellow);
    font-weight: 600; font-size: 28px; line-height: 36px;
  }
  .event-body {
    position: absolute; top: 262px; left: 118px; width: 492px;
    text-align: center; color: var(--text-light);
    font-weight: 700; font-size: 9.4px; line-height: 21px; text-transform: uppercase;
  }
  .event-side {
    position: absolute; top: 426px; width: 160px;
    text-align: center; color: var(--text-light);
    font-weight: 600; font-size: 9.6px; line-height: 12.5px;
  }
  .event-side--left { left: 52px; }
  .event-side--right { left: 518px; }

  /* back */
  .back-brand {
    position: absolute; top: 26px; left: 0; width: 100%;
    display: flex; flex-direction: column; align-items: center;
  }
  .back-brand .brand-mark { width: 54px; height: 54px; background: var(--brand-blue); margin-bottom: 20px; }
  .back-brand .brand-name { color: var(--brand-blue); font-size: 36px; }
  .back-brand .brand-tagline { color: var(--brand-blue); font-size: 13px; margin-top: 3px; }

  .faint-brand {
    position: absolute; color: var(--faint-brand);
    font-weight: 700; line-height: 1;
  }
  .faint-brand span { display: block; font-size: 15px; font-weight: 400; margin-top: 2px; letter-spacing: 0.5px; }
  .faint-brand--mid { left: 14px; top: 318px; font-size: 44px; }
  .faint-brand--low { left: 330px; top: 400px; font-size: 44px; }

  .web-band {
    position: absolute; left: 0; top: 462px; width: 100%; height: 36px;
    background: linear-gradient(90deg, rgba(255,255,255,0.2) 0%, var(--silver-light) 30%, var(--silver-light) 70%, rgba(255,255,255,0.3) 100%);
    display: flex; align-items: center; justify-content: center;
    color: var(--brand-dark); font-weight: 600; font-size: 20px;
  }
</style>
</head>
<body>
  <section class="invite-card invite-card--front">
    <div class="circuit-art" role="img" aria-label="Circuit-board traces with halftone dot corners in cyan on navy"></div>
    <div class="glow" style="left:110px;top:160px;width:90px;height:90px"></div>
    <div class="glow" style="left:420px;top:140px;width:80px;height:80px"></div>
    <header class="brand-band">
      <div class="brand-mark"></div>
      <div class="brand-name">CORVANDEL</div>
      <div class="brand-tagline">IT CONSULTING AND SERVICES</div>
    </header>
    <h1 class="event-title">MACHINE LEARNING AND<br>ARTIFICIAL INTELLIGENCE.</h1>
    <p class="event-body">Lorem ipsum dolor sit amet, consectetuer adipiscing elit, sed diam nonummy nibh euismod tincidunt ut laoreet dolore magna aliquam erat volutpat. Ut wisi enim ad minim veniam, quis nostrud exercitation ullamcorper suscipit lobortis nisl ut aliquip ex ea commodo consequat. Duis autem vel eum iriure dolor in hendrerit in vulputate velit esse molestie consequat, vel illum dolore eu feugiat nulla facilisis at vero eros et accumsan et iusto odio dignissim qui blandit praesent luptatum zzril delenit augue duis dolore te feugait nulla facilisi.</p>
    <p class="event-side event-side--left">Lorem ipsum dolor sit amet, consectetuer adipiscing elit, sed diam nonummy nibh euismod tincidunt ut laoreet dolore magna aliquam erat volutpat.</p>
    <p class="event-side event-side--right">Lorem ipsum dolor sit amet, consectetuer adipiscing elit, sed diam nonummy nibh euismod tincidunt ut laoreet dolore magna aliquam erat volutpat.</p>
  </section>

  <section class="invite-card invite-card--back">
    <div class="circuit-art" role="img" aria-label="Circuit-board traces with halftone dot corners in cyan on navy"></div>
    <div class="glow" style="left:240px;top:20px;width:80px;height:80px"></div>
    <div class="glow" style="left:520px;top:180px;width:90px;height:90px"></div>
    <div class="faint-brand faint-brand--mid">CORVANDEL<span>IT CONSULTING AND SERVICES</span></div>
    <div class="faint-brand faint-brand--low">CORVANDEL<span>IT CONSULTING AND SERVICES</span></div>
    <div class="back-brand">
      <div class="brand-mark"></div>
      <div class="brand-name">CORVANDEL</div>
      <div class="brand-tagline">IT CONSULTING AND SERVICES</div>
    </div>
    <div class="web-band">www.yourwebsite.com</div>
  </section>
</body>
</html>
```